Business to Business Website Homepage Design

Hi, My Web Developer is giving me designs that aren't quite taking my fancy as far as visual impact. I'd love to see designs come out which are simple, fresh and powerful.
I just want a PDF document that I can give to my web developer to follow, so this project is NOT to make a website, its to design the homepage.
I would like it to scroll down through different areas of my website on the homepage. Our colours are Blood Orange, White, Grey & Black.
I like these websites:
Simplicity
https://www.quenzaro.com/au/webapps/mpp/home
Our Team Section
http://bremlitch.com.au/
We'd like our logo on top left. Nav bar top right. Have an image which we can place a headline subject on + video icon which will pop out with a video and opt in for name and email with a heading so people know what they're opting in for.
The next section should have a lot of white space, this "What we do" which is 1) Grow in size so your business can get bigger 2) increase in value, so you maximise what your business is worth 3) Free up your time, so you can live the lifestyle you've always wanted. Our brief was we want image/text combo with a lot of white space,
Then we have our services
After Services, would like to have a "Why Work With Us" section
Then a testimonials section
Then "Our Team"
Then contact us.
Thats pretty much it, we'd just love some different ideas, these guys are almost there, but just need more impact.
Updates
Target Market(s)
Business Owners between $1m to $3m turnover
Industry/Entity Type
Business
Number of Pages Required
1 page
Look and feel
Each slider illustrates characteristics of the customer's brand and the style your logo design should communicate.

```html
<!DOCTYPE html>
<html lang="en">
<head>
<meta charset="utf-8">
<title>Lodestar Partners – Home</title>
<link href="https://fonts.googleapis.com/css2?family=Open+Sans:wght@300;400;600;700;800&display=swap" rel="stylesheet">
<style>
:root{
  --orange:#e8501f;
  --orange-dark:#d4421a;
  --ink:#222;
  --grey:#6b6b6b;
  --dark:#2a2c30;
  --blue:#1d86d8;
  --green:#5aa640;
  --red:#e2493a;
  --white:#fff;
}
*{box-sizing:border-box;margin:0;padding:0}
html,body{width:1200px;height:4724px;overflow:hidden}
body{font-family:"Open Sans",sans-serif;color:var(--ink);background:var(--white)}
section{position:relative;width:1200px;overflow:hidden}
.wrap{position:relative;width:1000px;margin:0 auto}
.ph{position:absolute;inset:0}
p{font-size:13px;line-height:1.7}

/* header + hero */
.hero{height:648px;color:var(--white)}
.hero .ph{background:linear-gradient(120deg,#4a4a4c 0%,#6c6762 45%,#3a3b3e 100%)}
.hero .shade{position:absolute;inset:0;background:rgba(20,20,22,.35)}
.topbar{position:absolute;top:0;left:0;right:0;height:86px;background:rgba(255,255,255,.96);z-index:2}
.topbar .wrap{height:86px;display:flex;align-items:center;justify-content:space-between}
.logo{display:flex;align-items:center;gap:10px;font-weight:800;font-size:24px;color:var(--orange);letter-spacing:1px;text-transform:uppercase}
.logo i{width:30px;height:30px;border-radius:50%;background:var(--orange);display:block}
.nav{display:flex;height:86px;list-style:none}
.nav li{display:flex;align-items:center;padding:0 28px;font-size:14px;color:#555}
.nav li.active{background:var(--orange);color:var(--white)}
.hero-title{position:absolute;top:300px;width:100%;text-align:center;font-size:38px;font-weight:400;letter-spacing:1px;z-index:1}
.hero-title b{color:var(--orange);font-weight:700}
.play{position:absolute;left:560px;top:380px;width:80px;height:80px;z-index:1}

/* what we do */
.grow{height:360px}
.rocket{position:absolute;left:120px;top:70px;width:230px;height:230px;border-radius:50%;background:radial-gradient(circle,#f3c3a6 0%,#f7e4da 60%,#fff 100%)}
.block-h{font-size:30px;font-weight:800;text-transform:uppercase}
.block-s{font-size:22px;font-weight:300;margin-bottom:22px}
.grow .text{position:absolute;left:560px;top:70px;width:540px;color:#555}
.grow .block-h{color:var(--ink)}
.grow p{margin-bottom:14px}

.value{height:336px;background:linear-gradient(100deg,var(--orange-dark),var(--orange) 60%,#ef6a2c);color:var(--white)}
.value .text{position:absolute;left:100px;top:70px;width:760px}

.freetime{height:408px;color:var(--white)}
.freetime .ph{background:linear-gradient(90deg,#222 0%,#3b3b3b 50%,#2a2a2a 100%)}
.freetime .text{position:absolute;right:100px;top:70px;width:880px;text-align:right}
.freetime p{margin-bottom:14px}

/* services */
.services{height:504px;background:var(--blue);color:var(--white)}
.sec-h{text-align:center;font-size:30px;font-weight:800;text-transform:uppercase;padding-top:60px}
.services .grid{position:absolute;left:100px;top:160px;width:1000px;display:grid;grid-template-columns:repeat(3,1fr);row-gap:50px}
.svc{display:flex;gap:18px}
.svc svg{flex:none}
.svc h4{font-size:15px;font-weight:700;text-transform:uppercase;margin-bottom:4px}
.svc p{font-size:12px;line-height:1.55;width:190px}

/* why */
.why{height:456px;color:var(--white)}
.why .ph{background:linear-gradient(100deg,#6aa83c 0%,#4d9f6f 45%,#2c8cc0 100%)}
.why .lead{position:relative;text-align:center;width:860px;margin:14px auto 0;font-size:12px}
.stats{position:absolute;left:100px;top:230px;width:1000px;display:flex;justify-content:space-around;text-align:center}
.stat strong{display:block;font-size:44px;font-weight:700;margin-top:8px}
.stat span{font-size:13px;text-transform:uppercase;letter-spacing:1px}

/* testimonials */
.testi{height:384px;color:var(--white)}
.testi .ph{background:linear-gradient(180deg,#2f2f31,#474542)}
.testi .sec-h{position:relative;padding-top:40px;font-size:26px}
.avatar{position:absolute;left:555px;top:100px;width:90px;height:90px;border-radius:50%;background:#c8b6a3;border:3px solid var(--white)}
.quote{position:absolute;left:240px;top:215px;width:720px;text-align:center}
.quote .mark{position:absolute;left:-50px;top:-20px;font-size:70px;font-weight:700;line-height:1}
.quote cite{display:block;font-style:normal;font-size:17px;margin-top:16px}

/* team */
.team{height:744px}
.team .sec-h{padding-top:72px;font-size:28px;color:var(--ink)}
.team-grid{position:absolute;left:100px;top:170px;width:1000px;display:grid;grid-template-columns:repeat(4,1fr);gap:14px}
.member{height:216px;background:linear-gradient(160deg,#e3e1de,#bdb8b2)}
.member:nth-child(2n){background:linear-gradient(160deg,#d8d6d3,#9e9994)}

/* contact */
.contact{height:744px;background:var(--red);color:var(--white)}
.contact .sec-h{padding-top:56px}
.details{position:absolute;left:440px;top:135px;list-style:none;font-size:13px}
.details li{display:flex;align-items:center;gap:12px;margin-bottom:12px}
.form{position:absolute;left:260px;top:240px;width:680px}
.row{display:flex;gap:20px;margin-bottom:14px}
.field{flex:1;height:36px;background:var(--white);color:#777;font-size:12px;padding:10px 12px}
.field.msg{height:150px}
.send{display:block;width:150px;height:36px;margin:26px auto 0;background:var(--white);color:var(--red);font-weight:700;font-size:13px;text-align:center;line-height:36px;text-transform:uppercase}

/* footer */
.footer{height:140px;border-top:1px solid #e6e6e6}
.footer .wrap{display:flex;align-items:center;justify-content:space-between;height:92px}
.footer .logo{font-size:18px}
.footer .logo i{width:22px;height:22px}
.flinks{display:flex;gap:20px;list-style:none;font-size:12px;color:#555;margin-left:40px;margin-right:auto}
.copy{font-size:12px;color:#777}
.fnote{text-align:center;font-size:11px;color:#888}
.fnote b{color:var(--orange);font-weight:400}
</style>
</head>
<body>

<section class="hero">
  <div class="ph" role="img" aria-label="Photo of a smiling businessman at an office desk"></div>
  <div class="shade"></div>
  <header class="topbar">
    <div class="wrap">
      <div class="logo"><i></i>Lodestar Partners</div>
      <ul class="nav">
        <li class="active">Home</li><li>Services</li><li>Clients</li><li>Jobs</li><li>Contact</li>
      </ul>
    </div>
  </header>
  <h1 class="hero-title">WELCOME ON <b>LODESTAR PARTNERS</b></h1>
  <svg class="play" viewBox="0 0 80 80"><circle cx="40" cy="40" r="37" fill="none" stroke="#fff" stroke-width="3"/><path d="M32 25 L56 40 L32 55Z" fill="#fff"/></svg>
</section>

<section class="grow">
  <div class="rocket" role="img" aria-label="Illustration of a rocket launching with flames"></div>
  <div class="text">
    <h2 class="block-h">Grow in size</h2>
    <div class="block-s">so your business can get bigger</div>
    <p>We help established owners build the systems, people and sales engines needed for steady growth. Our advisers work beside you to find new markets and lift every part of the business.</p>
    <p>With a clear plan and regular reviews, you know where the next stage of growth will come from and what it takes to get there.</p>
  </div>
</section>

<section class="value">
  <div class="text">
    <h2 class="block-h">Increase in value</h2>
    <div class="block-s">so you maximise what your business is worth</div>
    <p>We look at profit, cash flow and risk to raise the real worth of your company. Stronger numbers, tidy records and a business that runs without you make it far more valuable to buyers, lenders and partners when the time comes to decide.</p>
  </div>
</section>

<section class="freetime">
  <div class="ph" role="img" aria-label="Dark photo of a relaxed business owner at work"></div>
  <div class="text">
    <h2 class="block-h">Free up your time</h2>
    <div class="block-s">so you can live the lifestyle you've always wanted</div>
    <p>When your team and processes carry the daily load, you get your evenings and weekends back. We help you hand over tasks with confidence and step into the role only you can fill.</p>
    <p>Spend more time with family, on new ideas or simply on rest, while the business keeps moving forward with good people in charge.</p>
  </div>
</section>

<section class="services">
  <h2 class="sec-h">Our Services</h2>
  <div class="grid">
    <div class="svc"><svg width="56" height="56" viewBox="0 0 56 56"><circle cx="28" cy="28" r="26" fill="none" stroke="#fff" stroke-width="2"/><circle cx="28" cy="22" r="6" fill="#fff"/><path d="M17 40 Q28 26 39 40Z" fill="#fff"/></svg><div><h4>People</h4><p>Hire, train and keep the right team so your business runs well every day.</p></div></div>
    <div class="svc"><svg width="56" height="56" viewBox="0 0 56 56"><circle cx="28" cy="28" r="26" fill="none" stroke="#fff" stroke-width="2"/><circle cx="28" cy="28" r="9" fill="none" stroke="#fff" stroke-width="4" stroke-dasharray="4 3"/><circle cx="28" cy="28" r="3" fill="#fff"/></svg><div><h4>Business Systems</h4><p>Clear processes and tools that let work flow without you in the middle.</p></div></div>
    <div class="svc"><svg width="56" height="56" viewBox="0 0 56 56"><circle cx="28" cy="28" r="26" fill="none" stroke="#fff" stroke-width="2"/><path d="M20 38 h16 l-3-16 h-10z" fill="#fff"/><rect x="24" y="16" width="8" height="5" fill="#fff"/></svg><div><h4>Funding</h4><p>Find the right finance to back growth, stock and new opportunities.</p></div></div>
    <div class="svc"><svg width="56" height="56" viewBox="0 0 56 56"><circle cx="28" cy="28" r="26" fill="none" stroke="#fff" stroke-width="2"/><path d="M16 36 L24 28 L30 33 L40 20" fill="none" stroke="#fff" stroke-width="3"/></svg><div><h4>New Earning Streams</h4><p>Add products and services that lift revenue from clients you already have.</p></div></div>
    <div class="svc"><svg width="56" height="56" viewBox="0 0 56 56"><circle cx="28" cy="28" r="26" fill="none" stroke="#fff" stroke-width="2"/><circle cx="28" cy="28" r="12" fill="none" stroke="#fff" stroke-width="2"/><path d="M16 28 h24 M28 16 v24" stroke="#fff" stroke-width="2"/></svg><div><h4>New Markets</h4><p>Test and enter new regions and sectors with a plan that limits risk.</p></div></div>
    <div class="svc"><svg width="56" height="56" viewBox="0 0 56 56"><circle cx="28" cy="28" r="26" fill="none" stroke="#fff" stroke-width="2"/><rect x="18" y="22" width="20" height="16" fill="#fff"/><rect x="23" y="17" width="10" height="5" fill="none" stroke="#fff" stroke-width="2"/></svg><div><h4>New Businesses</h4><p>Buy or start related ventures that fit and strengthen your group.</p></div></div>
  </div>
</section>

<section class="why">
  <div class="ph" role="img" aria-label="Photo of a team meeting with green and blue colour overlay"></div>
  <h2 class="sec-h" style="position:relative">Why work with us</h2>
  <p class="lead">We have guided hundreds of owners through growth, sale and succession. Our advice is practical, tested and built around the goals you set for your business.</p>
  <div class="stats">
    <div class="stat"><svg width="40" height="40" viewBox="0 0 40 40"><circle cx="20" cy="14" r="7" fill="#fff"/><path d="M6 36 Q20 18 34 36Z" fill="#fff"/></svg><strong>235</strong><span>Followers</span></div>
    <div class="stat"><svg width="40" height="40" viewBox="0 0 40 40"><rect x="6" y="9" width="28" height="25" fill="none" stroke="#fff" stroke-width="3"/><path d="M6 16 h28" stroke="#fff" stroke-width="3"/></svg><strong>1980</strong><span>Since</span></div>
    <div class="stat"><svg width="40" height="40" viewBox="0 0 40 40"><circle cx="20" cy="20" r="15" fill="none" stroke="#fff" stroke-width="3"/><path d="M13 23 Q20 30 27 23" fill="none" stroke="#fff" stroke-width="3"/></svg><strong>221</strong><span>Happy Clients</span></div>
    <div class="stat"><svg width="40" height="40" viewBox="0 0 40 40"><rect x="7" y="14" width="26" height="20" fill="#fff"/><rect x="14" y="8" width="12" height="6" fill="none" stroke="#fff" stroke-width="3"/></svg><strong>365</strong><span>Projects</span></div>
  </div>
</section>

<section class="testi">
  <div class="ph" role="img" aria-label="Dark blurred office background"></div>
  <h2 class="sec-h">Our Testimonials</h2>
  <div class="avatar" role="img" aria-label="Portrait of the client giving the testimonial"></div>
  <blockquote class="quote">
    <span class="mark">&ldquo;</span>
    <p style="font-size:15px">I found Lodestar through a friend's advice and by reading their latest messages and listening to their short calls. I found out that the team made the right choice from day one, and they brought our business to a new level in less than a year.</p>
    <cite>Marcus Elden, Partner</cite>
  </blockquote>
</section>

<section class="team">
  <h2 class="sec-h">Our Team</h2>
  <div class="team-grid">
    <div class="member" role="img" aria-label="Team member photo"></div>
    <div class="member" role="img" aria-label="Team member photo"></div>
    <div class="member" role="img" aria-label="Team member photo"></div>
    <div class="member" role="img" aria-label="Team member photo"></div>
    <div class="member" role="img" aria-label="Team member photo"></div>
    <div class="member" role="img" aria-label="Team member photo"></div>
    <div class="member" role="img" aria-label="Team member photo"></div>
    <div class="member" role="img" aria-label="Team member photo"></div>
  </div>
</section>

<section class="contact">
  <h2 class="sec-h">Contact Us</h2>
  <ul class="details">
    <li><svg width="18" height="18" viewBox="0 0 18 18"><path d="M9 1 C4 1 3 5 3 7 C3 11 9 17 9 17 C9 17 15 11 15 7 C15 5 14 1 9 1Z" fill="#fff"/><circle cx="9" cy="7" r="2.5" fill="#e2493a"/></svg>141 Harlow Street, Brinmore VIC 3990, Australia</li>
    <li><svg width="18" height="18" viewBox="0 0 18 18"><rect x="1" y="4" width="16" height="11" fill="#fff"/><path d="M1 4 L9 10 L17 4" fill="none" stroke="#e2493a" stroke-width="1.5"/></svg>hello@lodestarpartners.example</li>
    <li><svg width="18" height="18" viewBox="0 0 18 18"><path d="M4 1 L7 1 L8 5 L6 7 Q8 11 11 12 L13 10 L17 11 L17 14 Q17 17 13 17 Q2 15 1 4 Q1 1 4 1Z" fill="#fff"/></svg>(03) 5550 1928</li>
  </ul>
  <div class="form">
    <div class="row"><div class="field">Name</div><div class="field">Email Address</div></div>
    <div class="row"><div class="field">Phone Number</div><div class="field">Subject</div></div>
    <div class="row"><div class="field msg">Message</div></div>
    <span class="send">Send</span>
  </div>
</section>

<footer class="footer">
  <div class="wrap">
    <div class="logo"><i></i>Lodestar Partners</div>
    <ul class="flinks"><li>Home</li><li>Services</li><li>Clients</li><li>Jobs</li><li>Contact Us</li></ul>
    <div class="copy">Copyright © lodestarpartners.example 2024</div>
  </div>
  <p class="fnote">Lodestar Partners helps owners of growing companies build value, free up time and plan ahead. <b>Terms and privacy policy apply.</b></p>
</footer>

</body>
</html>
```